A taxi bidding business needs Web Design

We need a cutting edge, super UX-intuitive, Elegant web design for our business called Fyrelo.

Fyrelo is Australia based Kind of "Next Vantro" business where user creates a trip and cabs/drivers place bids on fares/bookings/trips and lowest bidder gets the job.
User can also share the Cabs going in same route to get lowest bids.

- The design needs to be very, very intuitive to use and navigate. Please do not use much of yellow color.

References: HomQuel & Vantro

Please see the attached pdf, attaching logo as well.

Ride Sharing, Taxi

Business

5+ page

Must have
• Icons/graphics, How it works icons, case studies icons, all mentioned pages
Should not have
• Not much yellow color

```html
<!DOCTYPE html>
<html lang="en">
<head>
<meta charset="utf-8">
<title>Fyrelo – Sign In</title>
<link href="https://fonts.googleapis.com/css2?family=Open+Sans:wght@300;400;600&family=Roboto:wght@400;500&display=swap" rel="stylesheet">
<style>
  :root{
    --nav:#1f0c0c;
    --navy:#1a2a6c;
    --navy-panel:#1c2b5e;
    --navy-field:#121c44;
    --red:#e8202a;
    --page:#ffffff;
    --modal:#eeeeee;
    --ink:#333333;
    --muted:#7a7a7a;
    --overlay:rgba(0,0,0,0.7);
  }
  *{margin:0;padding:0;box-sizing:border-box}
  html,body{width:1153px;height:1200px;overflow:hidden}
  body{position:relative;background:var(--page);font-family:"Open Sans",sans-serif;color:var(--ink)}
  .abs{position:absolute}

  .topbar{left:0;top:0;width:1153px;height:39px;background:var(--nav);z-index:30}
  .topbar a{position:absolute;top:9px;color:#8d8383;font-size:14.5px;text-decoration:none}
  .menu-icon{left:71px;top:11px}

  .brand{left:83px;top:72px}
  .brand-dot{position:absolute;left:52px;top:0;width:34px;height:34px;border-radius:50%;background:var(--red)}
  .brand-name{position:absolute;left:0;top:68px;font-size:26px;font-weight:600;color:var(--navy);letter-spacing:1px}
  .page-title{left:339px;top:70px;font-size:59px;font-weight:300;color:var(--navy);line-height:1}
  .title-rule{left:339px;top:154px;width:731px;height:1px;background:#666}

  .hero{left:71px;top:202px;width:1012px;height:318px;background:linear-gradient(120deg,#a88d68,#6f7150 45%,#8b7a57 75%,#9a8f6c)}

  .signup-panel{left:167px;top:475px;width:819px;height:393px;background:var(--navy-panel)}
  .field{position:absolute;background:var(--navy-field);border:1px solid #2b3a70;color:#7a86b0;font-size:11px;padding:10px 18px}
  .signup-btn{left:435px;top:728px;width:298px;height:34px;background:var(--red);color:#fff;font-size:14px;font-weight:600;padding:8px 20px;display:flex;justify-content:space-between;align-items:center}
  .alt-line{left:167px;top:776px;width:819px;text-align:center;font-size:10px;color:#c9d0e6}
  .legal{left:380px;top:796px;width:393px;text-align:center;font-size:7.6px;line-height:12.7px;color:#aeb6d2}

  .feature{position:absolute;top:943px;width:310px;text-align:center}
  .feature-icon{width:93px;height:86px;margin:0 auto;background:#f2f2f2;display:flex;align-items:center;justify-content:center}
  .feature-title{margin-top:22px;font-family:"Roboto",sans-serif;font-weight:500;font-size:14.5px;color:var(--navy)}
  .feature-rule{width:66px;height:2px;background:var(--red);margin:7px auto 0}
  .feature-body{margin-top:16px;font-family:"Roboto",sans-serif;font-size:12.6px;line-height:16px;color:#666}

  .overlay{left:0;top:39px;width:1153px;height:1161px;background:var(--overlay);z-index:10}

  .modal{left:137px;top:136px;width:844px;height:429px;background:var(--modal);z-index:20}
  .modal-title{position:absolute;left:0;top:44px;width:100%;text-align:center;font-size:56px;font-weight:300;color:var(--navy);line-height:1.2}
  .modal-rule{position:absolute;left:360px;top:122px;width:124px;height:2px;background:var(--red)}
  .role{position:absolute;top:202px;width:300px}
  .role h2{font-size:28px;font-weight:300;color:var(--navy);line-height:1.2}
  .role p{margin-top:9px;margin-left:2px;font-size:14.3px;line-height:19.5px;color:var(--ink)}
  .role-btn{margin-top:13px;width:171px;height:34px;background:var(--red);color:#fff;font-size:13.5px;font-weight:600;display:flex;align-items:center;justify-content:space-between;padding:0 12px 0 20px;letter-spacing:.3px}
</style>
</head>
<body>

<nav class="topbar abs">
  <svg class="menu-icon abs" width="26" height="16" viewBox="0 0 26 16"><g fill="#8d8383"><rect width="26" height="3"/><rect y="6.5" width="26" height="3"/><rect y="13" width="26" height="3"/></g></svg>
  <a style="left:167px">Ride</a>
  <a style="left:230px">Drive</a>
  <a style="left:948px">Help</a>
  <a style="left:1012px">Sign In</a>
</nav>

<div class="brand abs">
  <span class="brand-dot"></span>
  <span class="brand-name">Fyrelo</span>
</div>
<h1 class="page-title abs">Roam Around</h1>
<div class="title-rule abs"></div>

<div class="hero abs" role="img" aria-label="Close-up photograph of an old paper map"></div>

<section class="signup-panel abs">
  <div class="field" style="left:34px;top:74px;width:364px;height:35px">First Name</div>
  <div class="field" style="left:34px;top:117px;width:364px;height:35px">Last Name</div>
  <div class="field" style="left:34px;top:159px;width:364px;height:35px">Email</div>
  <div class="field" style="left:34px;top:203px;width:364px;height:35px">Phone</div>
  <div class="field" style="left:417px;top:74px;width:364px;height:35px">Create Password</div>
  <div class="field" style="left:417px;top:117px;width:364px;height:35px">City</div>
  <div class="field" style="left:417px;top:187px;width:364px;height:49px">Invite Code (optional)</div>
</section>
<div class="signup-btn abs"><span>SIGN UP TO DRIVE</span><span>&#10230;</span></div>
<p class="alt-line abs">OR SIGN UP WITH YOUR RIDER ACCOUNT.</p>
<p class="legal abs">By proceeding, I agree that Vantro or its representatives may contact me by email, phone, or SMS (including by automatic telephone dialing system) at the email address or number I provide, including for marketing purposes. I have read and understand the relevant Driver Privacy Statement.</p>

<div class="feature" style="left:84px">
  <div class="feature-icon">
    <svg width="56" height="44" viewBox="0 0 56 44" fill="none" stroke="#555" stroke-width="2.5"><rect x="8" y="4" width="28" height="26"/><path d="M36 14h10l7 9v7H36z"/><circle cx="16" cy="35" r="5"/><circle cx="44" cy="35" r="5"/><path d="M0 12h6M2 20h6"/></svg>
  </div>
  <h3 class="feature-title">INSTANT BIDS, SLASHED FARES</h3>
  <div class="feature-rule"></div>
  <p class="feature-body">Lorem ipsum dolor sit amet, consectetur adipiscing elit. Fusce vestibulum sagittis finibus. Phasellus tempor, lorem et egestas vulputate, nunc dolor luctus felis, ornare pellentesque nisl eros quis risus.</p>
</div>
<div class="feature" style="left:421px">
  <div class="feature-icon">
    <svg width="56" height="50" viewBox="0 0 56 50" fill="#555"><rect x="2" y="2" width="52" height="10"/><rect x="8" y="12" width="6" height="18"/><rect x="42" y="12" width="6" height="18"/><rect x="18" y="12" width="20" height="36" fill="#777"/><circle cx="31" cy="38" r="5" fill="#555"/></svg>
  </div>
  <h3 class="feature-title">AUTOMATED BIDDING, SAVES TIME</h3>
  <div class="feature-rule"></div>
  <p class="feature-body">Lorem ipsum dolor sit amet, consectetur adipiscing elit. Fusce vestibulum sagittis finibus. Phasellus tempor, lorem et egestas vulputate, nunc dolor luctus felis, ornare pellentesque nisl eros quis risus.</p>
</div>
<div class="feature" style="left:759px">
  <div class="feature-icon">
    <svg width="64" height="50" viewBox="0 0 64 50"><path d="M4 30l6-12h28l6 12v10H4z" fill="#555"/><circle cx="14" cy="40" r="5" fill="#999"/><circle cx="36" cy="40" r="5" fill="#999"/><path d="M50 4l6 6-4 4v26" stroke="#555" stroke-width="5" fill="none"/></svg>
  </div>
  <h3 class="feature-title">SPEEDY SERVICE ANYWHERE, ANYTIME</h3>
  <div class="feature-rule"></div>
  <p class="feature-body">Lorem ipsum dolor sit amet, consectetur adipiscing elit. Fusce vestibulum sagittis finibus. Phasellus tempor, lorem et egestas vulputate, nunc dolor luctus felis, ornare pellentesque nisl eros quis risus.</p>
</div>

<div class="overlay abs"></div>

<section class="modal abs">
  <h2 class="modal-title">Sign In</h2>
  <div class="modal-rule"></div>
  <div class="role" style="left:64px">
    <h2>Driver</h2>
    <p>Find everything you need to track your success on the road.</p>
    <div class="role-btn"><span>DRIVER SIGN IN</span><span>&#10230;</span></div>
  </div>
  <div class="role" style="left:510px">
    <h2>Rider</h2>
    <p>Manage your payment options, review trip history.and more.</p>
    <div class="role-btn"><span>RIDER SIGN IN</span><span>&#10230;</span></div>
  </div>
</section>

</body>
</html>
```